The Brightwater Hour with Dale Morrow

Create Podcast Art for Podvale. My podcast is about overcoming adversities.

Everyone's adversity is different and there's no one-size-fits-all solution, but when you hear someone's else's story of resilience and add a little salt to it, you can find the inspiration you need to write a new ending to your struggle.

Maybe you're going through something right now and you're afraid:

● You won't be successful
● People are talking behind your back
● You'll never get the help you need
● You're not a good husband or wife
● Your child is out of control and you'll never get through to him or her
● There isn't a light at the end of your tunnel
● You'll never get your finances out of the red
● Your spouse won't ever see things your way
● The world is never gonna change

Every story we tell on The Brightwater Hour podcast challenges those thoughts, because everyday people going through everyday stuff just like you show us otherwise.

This podcast is for you. And, it's different.

Most interviews I do, I try to go on location and interview in person.

You might not see us together on the screen,
but you'll sense the raw sincerity and closeness of a side-by-side interview through your speakers.

The colors I have chosen below are close to the website colors. If you need a better view of that go here http://www.dalemorrowvoice.com

I've attached two pictures for the podcast. I'm not sure which one to use just yet so I put them both here to see what i created by your great people!

Target Market(s)

People who are currently going through an Advesirty or have been through one. 28 - 40 age group.

Colors
ec1f27
ffffff
000000
fbee3e

Requirements
Must have
• Eye appeal and The title "The Brightwater Hour" with Dale Morrow
• HAS to be stand-out, and it HAS to give a great first impression.
Nice to have
• The colors I have chosen are close to the website colors.

```html
<!DOCTYPE html>
<html lang="en">
<head>
<meta charset="utf-8">
<title>The Brightwater Hour – Podcast Art</title>
<link rel="stylesheet" href="https://fonts.googleapis.com/css2?family=Arimo:wght@400&family=Open+Sans:wght@700&display=swap">
<style>
  :root {
    --night-navy: #1b1a3c;
    --signal-yellow: #fbee3e;
    --ink-black: #000000;
    --paper-white: #ffffff;
    --shadow: rgba(0, 0, 0, 0.55);
  }
  html, body {
    margin: 0;
    padding: 0;
    width: 1195px;
    height: 1200px;
    overflow: hidden;
    background: var(--night-navy);
  }
  .podcast-art {
    position: relative;
    width: 1195px;
    height: 1200px;
    background: var(--night-navy);
    overflow: hidden;
  }
  .title-card {
    position: absolute;
    left: 110px;
    top: 28px;
    width: 835px;
    height: 428px;
    box-sizing: border-box;
    padding-top: 34px;
    background: var(--signal-yellow);
    border: 7px solid var(--paper-white);
    box-shadow: 10px 10px 14px var(--shadow);
    text-align: center;
  }
  .show-title {
    margin: 0;
    font-family: "Arimo", Arial, sans-serif;
    font-weight: 400;
    font-size: 86px;
    line-height: 1.15;
    color: var(--ink-black);
  }
  .show-host {
    margin: 14px 0 0;
    font-family: "Arimo", Arial, sans-serif;
    font-weight: 400;
    font-size: 46px;
    color: var(--ink-black);
  }
  .support-card {
    position: absolute;
    left: 178px;
    top: 405px;
    width: 960px;
    height: 270px;
    box-sizing: border-box;
    background: var(--signal-yellow);
    border: 7px solid var(--paper-white);
    box-shadow: 10px 10px 14px var(--shadow);
    transform: rotate(4deg);
    display: flex;
    align-items: center;
    justify-content: center;
  }
  .support-line {
    margin: 0;
    font-family: "Open Sans", Arial, sans-serif;
    font-weight: 700;
    font-size: 68px;
    letter-spacing: -2px;
    color: var(--ink-black);
    white-space: nowrap;
  }
  .together-badge {
    position: absolute;
    left: 0;
    top: 0;
    width: 1195px;
    height: 1200px;
  }
  .badge-fill { fill: var(--ink-black); stroke: var(--paper-white); stroke-width: 7; }
  .brand-mark { fill: var(--signal-yellow); }
  .brand-name {
    font-family: "Open Sans", Arial, sans-serif;
    font-weight: 700;
    font-size: 52px;
    fill: var(--signal-yellow);
  }
  .badge-word {
    font-family: "Open Sans", Arial, sans-serif;
    font-weight: 700;
    font-size: 104px;
    letter-spacing: -3px;
    fill: var(--paper-white);
  }
</style>
</head>
<body>
  <main class="podcast-art">
    <div class="title-card">
      <h1 class="show-title">"The Brightwater<br>Hour" ?</h1>
      <p class="show-host">with Dale Morrow</p>
    </div>

    <div class="support-card">
      <p class="support-line">WE STAND BY YOU</p>
    </div>

    <svg class="together-badge" viewBox="0 0 1195 1200" aria-label="Together badge">
      <ellipse class="badge-fill" cx="492" cy="930" rx="478" ry="205" transform="rotate(-17 492 930)"/>
      <rect class="brand-mark" x="348" y="800" width="40" height="40"/>
      <text class="brand-name" x="402" y="838">Tidewell</text>
      <text class="badge-word" x="510" y="1010" text-anchor="middle" transform="rotate(-12 510 975)">TOGHETHER</text>
    </svg>
  </main>
</body>
</html>
```